Film and TV production company

I have the logo already designed by craft nest. I just need the text and the logo attached to the business card. Maybe a small design on the back of the card or text.

Industry/Entity Type

film tv arts

Contact Information for Business Card

Brent Walcott Cinematographer-Director

Colors
F0912C
F2A743
F7CA91
FBE8D2
FDF5EE
EE7325
F08F49
F5BC92
FAE3D3
FDF4ED

Requirements
Must have
• www.bluewattlestudio.com.au my email address mail@bluewattlestudio.com.au my mobile number 0412573984
Nice to have
• Some kind of small art work on the back that ties in with the logo design attached
Should not have
• Must clean and simple

```html
<!DOCTYPE html>
<html lang="en">
<head>
<meta charset="utf-8">
<title>Blue Wattle Studio – Business Card</title>
<link href="https://fonts.googleapis.com/css2?family=Montserrat:wght@400&family=Arimo:wght@400;700&display=swap" rel="stylesheet">
<style>
  :root {
    --stage: #c2c2c2;
    --card-white: #ffffff;
    --ink-dark: #222222;
    --band-dark: #1f1f1f;
    --back-dark: #242424;
    --back-warm: #2f2a25;
    --back-green: rgba(60, 80, 50, 0.18);
    --back-slate: rgba(70, 80, 90, 0.25);
    --accent-orange: #e88224;
    --accent-green: #5e9e3a;
    --text-light: #ffffff;
  }
  * { box-sizing: border-box; margin: 0; padding: 0; }
  html, body { width: 1200px; height: 788px; overflow: hidden; }
  body {
    background: var(--stage);
    display: flex;
    align-items: center;
    justify-content: center;
    gap: 40px;
    font-family: "Montserrat", sans-serif;
  }
  .card {
    position: relative;
    width: 540px;
    height: 310px;
    border-radius: 18px;
    overflow: hidden;
  }

  /* Front */
  .card--front { background: var(--card-white); }
  .front__orange-block {
    position: absolute;
    right: 0; top: 0;
    width: 130px; height: 145px;
    background: var(--accent-orange);
  }
  .front__band {
    position: absolute;
    left: 0; top: 145px;
    width: 470px; height: 130px;
    background: var(--band-dark);
  }
  .company-name {
    position: absolute;
    font-family: "Montserrat", sans-serif;
    font-weight: 400;
    white-space: nowrap;
  }
  .card--front .company-name {
    left: 32px; top: 62px;
    font-size: 26px;
    color: var(--ink-dark);
  }

  .contact { position: absolute; left: 32px; top: 157px; font-family: "Arimo", sans-serif; }
  .contact__name {
    color: var(--accent-green);
    font-weight: 700;
    font-size: 21px;
    line-height: 24px;
  }
  .contact__role { color: var(--text-light); font-size: 13px; line-height: 16px; margin-top: 2px; }
  .contact__list { list-style: none; margin-top: 8px; }
  .contact__item {
    display: flex; align-items: center; gap: 8px;
    color: var(--text-light); font-size: 12.5px; line-height: 19px;
  }
  .contact__icon { width: 12px; height: 12px; flex: none; }

  /* Back */
  .card--back {
    background: linear-gradient(160deg, var(--back-dark) 0%, var(--back-dark) 45%, var(--back-warm) 100%);
  }
  .back__band {
    position: absolute;
    inset: 0;
  }
  .back__band--green {
    background: var(--back-green);
    clip-path: polygon(0 62%, 100% 25%, 100% 55%, 0 100%);
  }
  .back__band--slate {
    background: var(--back-slate);
    clip-path: polygon(88% 25%, 100% 20%, 100% 100%, 70% 100%);
  }
  .card--back .company-name {
    left: 0; right: 0; top: 138px;
    text-align: center;
    font-size: 32px;
    color: var(--text-light);
  }
</style>
</head>
<body>

  <section class="card card--front" aria-label="Business card front">
    <div class="front__orange-block"></div>
    <div class="front__band"></div>

    <div class="company-name">Blue Wattle Studio</div>

    <div class="contact">
      <div class="contact__name">BRENT WALCOTT</div>
      <div class="contact__role">Cinematographer-Director</div>
      <ul class="contact__list">
        <li class="contact__item">
          <svg class="contact__icon" viewBox="0 0 12 12"><circle cx="6" cy="6" r="6" fill="var(--accent-orange)"/><path d="M3.6 3.2h1.4l.6 1.5-.8.6a4 4 0 0 0 1.9 1.9l.6-.8 1.5.6v1.4c-3 .3-5.5-2.2-5.2-5.2z" fill="var(--band-dark)"/></svg>
          0412573984
        </li>
        <li class="contact__item">
          <svg class="contact__icon" viewBox="0 0 12 12"><rect x="0" y="2" width="12" height="8" fill="var(--accent-orange)"/><path d="M0 2l6 4.5L12 2" fill="none" stroke="var(--band-dark)" stroke-width="1"/></svg>
          mail@bluewattlestudio.com.au
        </li>
        <li class="contact__item">
          <svg class="contact__icon" viewBox="0 0 12 12"><circle cx="6" cy="6" r="6" fill="var(--accent-orange)"/><path d="M1 6h10M6 1c-2 2.5-2 7.5 0 10M6 1c2 2.5 2 7.5 0 10" fill="none" stroke="var(--band-dark)" stroke-width="0.9"/></svg>
          www.bluewattlestudio.com.au
        </li>
      </ul>
    </div>
  </section>

  <section class="card card--back" aria-label="Business card back">
    <div class="back__band back__band--green"></div>
    <div class="back__band back__band--slate"></div>
    <div class="company-name">Blue Wattle Studio</div>
  </section>

</body>
</html>
```